Infectious Diseases Research Laboratory Needs Business Card

We need a business card for an academic research laboratory based in Kansas City called VELKOR. The full lab name is Microbe Exposure Kinetics/Response Modeling Integrated Study Laboratory, but this does not need to be incorporated. We study novel ways to optimize the treatment of multidrug-resistant bacterial infections ("superbugs") throughout the entire biomedical research spectrum (from benchtop to bedside). The name VELKOR is not only an acronym for our lab name, but also represents our desire to make discoveries and explore the unknown (the stars, if you well). It also serves as an ode to the state of Kansas motto where we are based, ad astra per aspera ("to the stars, through difficulty").

Target Market(s)

Pharmaceutical companies, researchers

Industry/Entity Type

Pharmaceutical

Contact Information for Business Card

The business card should incorporate and complement our new logo (see uploaded files). Double-sided designs are preferred. Looking for something modern, but professional.

Font styles to use
Sans Serif

Requirements
Must have
• Double-sided. One side would ideally be a solid color incorporating logo and the other should also have the logo (smaller), but incorporate staff information.
• Color codes:
• Red: #F04C51
• Blue: #3477B5
• Gray: #808285

```html
<!DOCTYPE html>
<html lang="en">
<head>
<meta charset="utf-8">
<title>VELKOR Business Card</title>
<link rel="stylesheet" href="https://fonts.googleapis.com/css2?family=Josefin+Sans:wght@400;600&family=Work+Sans:wght@400;500;600&display=swap">
<style>
  :root {
    --red: #F04C51;
    --blue: #3477B5;
    --gray: #808285;
    --ink: #2b2b2b;
    --paper: #ffffff;
    --backdrop: #e6e7e8;
  }
  * { margin: 0; padding: 0; box-sizing: border-box; }
  html, body { width: 1200px; height: 900px; overflow: hidden; background: var(--backdrop); }
  .canvas { position: relative; width: 1200px; height: 900px; }

  .card {
    position: absolute;
    left: 280px;
    width: 640px;
    height: 366px;
    box-shadow: 0 6px 18px rgba(0,0,0,0.18);
    overflow: hidden;
  }

  /* Back side */
  .card-back { top: 60px; background: var(--blue); color: var(--paper); }
  .back-brand {
    position: absolute; left: 0; right: 0; top: 130px;
    display: flex; align-items: center; justify-content: center; gap: 18px;
  }
  .brand-dot { width: 34px; height: 34px; border-radius: 50%; background: var(--paper); }
  .back-brand .brand-name {
    font-family: "Josefin Sans", sans-serif; font-weight: 400;
    font-size: 64px; letter-spacing: 6px; line-height: 1; padding-top: 8px;
  }
  .back-url {
    position: absolute; left: 0; right: 0; top: 270px; text-align: center;
    font-family: "Work Sans", sans-serif; font-size: 17px; letter-spacing: 1.5px;
  }

  /* Front side */
  .card-front { top: 474px; background: var(--paper); }
  .front-brand { position: absolute; left: 36px; top: 118px; width: 300px; }
  .front-brand .brand-row { display: flex; align-items: center; gap: 12px; }
  .front-brand .brand-dot { width: 26px; height: 26px; background: var(--red); }
  .front-brand .brand-name {
    font-family: "Josefin Sans", sans-serif; font-weight: 400; color: var(--red);
    font-size: 54px; letter-spacing: 4px; line-height: 1; padding-top: 6px;
  }
  .lab-name {
    margin-top: 14px;
    font-family: "Josefin Sans", sans-serif; font-weight: 400; color: var(--blue);
    font-size: 12.5px; letter-spacing: 1.2px; text-transform: uppercase; line-height: 1.5;
  }
  .divider { position: absolute; left: 356px; top: 88px; width: 1.5px; height: 170px; background: var(--blue); }

  .contact { position: absolute; left: 380px; top: 90px; font-family: "Work Sans", sans-serif; color: var(--ink); }
  .person-name { font-weight: 600; font-size: 24px; color: var(--red); line-height: 1.1; }
  .person-role { font-size: 16px; color: var(--ink); margin-bottom: 16px; }
  .address { font-size: 14.5px; line-height: 1.35; letter-spacing: 0.5px; margin-bottom: 14px; }
  .contact-list { list-style: none; font-size: 14.5px; letter-spacing: 0.5px; }
  .contact-list li { display: flex; align-items: center; gap: 12px; height: 24px; }
  .contact-list svg { width: 14px; height: 14px; flex: none; }
  .accent { color: var(--blue); }

  .base-band { position: absolute; left: 0; right: 0; bottom: 0; height: 12px; display: flex; }
  .base-band .band-red { width: 47%; background: var(--red); }
  .base-band .band-blue { flex: 1; background: var(--blue); }
</style>
</head>
<body>
<main class="canvas">
  <section class="card card-back" aria-label="Card back">
    <div class="back-brand">
      <span class="brand-dot"></span>
      <span class="brand-name">VELKOR</span>
    </div>
    <p class="back-url">www.velkor.com</p>
  </section>

  <section class="card card-front" aria-label="Card front">
    <div class="front-brand">
      <div class="brand-row">
        <span class="brand-dot"></span>
        <span class="brand-name">VELKOR</span>
      </div>
      <p class="lab-name">Microbe Exposure Kinetics/Response Modeling Integrated Study Laboratory</p>
    </div>

    <div class="divider"></div>

    <div class="contact">
      <h1 class="person-name">Dana Whitfield</h1>
      <p class="person-role">Founder</p>
      <p class="address">240 E Maple Ave<br>Linwood, KS 66052</p>
      <ul class="contact-list">
        <li>
          <svg viewBox="0 0 14 14" aria-hidden="true"><rect x="3" y="0.8" width="8" height="12.4" rx="1.5" fill="none" stroke="#F04C51" stroke-width="1.4"/><line x1="6" y1="11" x2="8" y2="11" stroke="#F04C51" stroke-width="1.2"/></svg>
          <span>(555) 018-4421</span>
        </li>
        <li>
          <svg viewBox="0 0 14 14" aria-hidden="true"><rect x="0.5" y="2.5" width="13" height="9" fill="#F04C51"/><polyline points="0.5,2.5 7,8 13.5,2.5" fill="none" stroke="#fff" stroke-width="1.2"/></svg>
          <span>hello@danawhitfield.com</span>
        </li>
        <li>
          <svg viewBox="0 0 14 14" aria-hidden="true"><g fill="none" stroke="#F04C51" stroke-width="1.2"><circle cx="7" cy="7" r="6"/><ellipse cx="7" cy="7" rx="2.6" ry="6"/><line x1="1" y1="7" x2="13" y2="7"/><line x1="2" y1="4" x2="12" y2="4"/><line x1="2" y1="10" x2="12" y2="10"/></g></svg>
          <span>www.<span class="accent">velkor</span>.org</span>
        </li>
      </ul>
    </div>

    <div class="base-band"><span class="band-red"></span><span class="band-blue"></span></div>
  </section>
</main>
</body>
</html>
```